Commercial printing and sign company printed advertisement.

We're wanting a new look for our printed advertisements. We've been in business for 40 years and have been pushing hard the last couple of years to grow our business. Our target market is changing and our client base is changing. I am looking for advertisement that appeals to larger companies. However, we are not stuffy people so I would like the ads to convey our professionalism but also stand out with color and have a fun side. I'm currently needing advertisements for a printed magazine, printed newspaper, web ads and a table top at a local restaurant. We have our traditional four color logo (swoosh) as well as a simpler single color option. I am attaching various ads we have done previously so you can see what we have. It is important for these ads to convey the different things we do - as we do alot!

```html
<!DOCTYPE html>
<html lang="en">
<head>
<meta charset="utf-8">
<title>Brightline Printing – Creative Print & Design Hub</title>
<link rel="stylesheet" href="https://fonts.googleapis.com/css2?family=Oswald:wght@500;600;700&family=Barlow+Condensed:ital,wght@0,500;0,600;0,700;1,600;1,700&family=Montserrat:wght@600&display=swap">
<style>
  :root{
    --navy:#0b0b5c;
    --ink:#2e2e2e;
    --sky:#22b8ee;
    --sky-light:#3fb4ec;
    --orange:#f28a30;
    --pink:#e8318e;
    --green:#14a85a;
    --service-green:#13a04c;
    --plum:#a0508f;
    --brand-red:#d3202f;
    --white:#ffffff;
  }
  *{margin:0;padding:0;box-sizing:border-box}
  html,body{width:927px;height:1200px;overflow:hidden;background:var(--white)}
  .ad{position:relative;width:927px;height:1200px;overflow:hidden;background:var(--white);font-family:"Barlow Condensed",sans-serif;color:var(--ink)}

  .hero-photo{position:absolute;left:0;top:0}
  .brand-name{position:absolute;left:300px;top:34px;font-family:"Barlow Condensed",sans-serif;font-weight:700;font-size:30px;color:var(--brand-red);letter-spacing:.5px}

  .headline{position:absolute;right:54px;top:72px;text-align:right;font-family:"Oswald",sans-serif;font-weight:700;color:var(--navy);line-height:.98;letter-spacing:-1.5px}
  .headline .lead{display:block;font-size:54px;font-weight:600}
  .headline .main{display:block;font-size:62px}

  .service-card{position:absolute;width:191px;border:4px solid;border-radius:14px;background:var(--white);overflow:hidden}
  .service-card h3{font-family:"Barlow Condensed",sans-serif;font-weight:600;font-size:25px;color:var(--white);padding:12px 0 4px 12px;line-height:1.1}
  .service-card ul{list-style:none;padding:4px 0 0 8px}
  .service-card li{font-weight:600;font-size:20px;line-height:27px;color:#111;white-space:nowrap}
  .service-card li::before{content:"•";display:inline-block;width:22px;font-size:16px}
  .card-print{left:477px;top:284px;height:312px;border-color:var(--sky)}
  .card-print h3{background:var(--sky)}
  .card-large{left:678px;top:284px;height:312px;border-color:var(--orange)}
  .card-large h3{background:var(--orange)}
  .card-apparel{left:477px;top:614px;height:314px;border-color:var(--pink)}
  .card-apparel h3{background:var(--pink)}
  .card-apparel ul{padding-top:2px}
  .card-promo{left:678px;top:614px;height:314px;border-color:var(--green)}
  .card-promo h3{background:var(--green);padding:11px 0 3px 12px}
  .card-promo ul{padding-top:1px}
  .card-promo li{line-height:25.5px}

  .why-title{position:absolute;left:0;width:506px;top:488px;text-align:center;font-family:"Barlow Condensed",sans-serif;font-weight:700;font-size:44px;color:var(--ink)}
  .reason{position:absolute;left:65px;width:330px}
  .reason h4{font-weight:700;font-size:29px;line-height:1.05;letter-spacing:-.4px}
  .reason p{font-weight:600;font-size:21px;line-height:25px;color:#3a3a3a;letter-spacing:-.3px}
  .reason-service{top:545px}
  .reason-service h4{color:var(--service-green)}
  .reason-shop{top:656px}
  .reason-shop h4{color:var(--pink)}
  .reason-experience{top:769px}
  .reason-experience h4{color:var(--plum)}

  .specialized{position:absolute;left:67px;top:903px;width:322px;height:138px;border:4px solid var(--navy);border-radius:12px;font-family:"Montserrat",sans-serif;font-weight:600;color:#3a3a3a}
  .specialized h5{position:absolute;left:20px;top:-17px;background:var(--white);padding:0 8px;font-size:21px;font-weight:600;color:#3a3a3a}
  .specialized ul{list-style:none;position:absolute;left:32px;top:17px;font-size:17.5px;line-height:21.5px}

  .trust{position:absolute;left:478px;top:938px;font-family:"Barlow Condensed",sans-serif;font-style:italic;color:var(--ink)}
  .trust .claim{display:block;font-weight:700;font-size:42px;letter-spacing:-.5px;line-height:1}
  .trust .since{display:block;font-weight:600;font-size:38px;margin:6px 0 0 8px;line-height:1}

  .footer-band{position:absolute;left:0;top:1050px;width:927px;height:150px}
  .footer-text{position:absolute;left:0;top:1104px;width:927px;text-align:center;font-family:"Barlow Condensed",sans-serif}
  .footer-text .slogan{display:block;font-weight:700;font-size:29px;color:var(--sky-light);letter-spacing:-.3px}
  .footer-text .contact{display:block;font-weight:500;font-size:30px;color:var(--white);margin-top:2px}
</style>
</head>
<body>
<div class="ad">

  <svg class="hero-photo" width="540" height="490" viewBox="0 0 540 490">
    <defs>
      <linearGradient id="photoTone" x1="0" y1="0" x2="1" y2="1">
        <stop offset="0" stop-color="#8d959c"/>
        <stop offset=".45" stop-color="#c9c6c2"/>
        <stop offset=".75" stop-color="#5b6a86"/>
        <stop offset="1" stop-color="#d6a33a"/>
      </linearGradient>
    </defs>
    <path role="img" aria-label="Photo of a print technician pressing colourful transfers onto t-shirts beside mugs, cards and a wide-format printer" d="M0 0 H527 A527 465 0 0 1 0 465 Z" fill="url(#photoTone)"/>
    <path d="M527 0 A527 465 0 0 1 0 465" fill="none" stroke="var(--sky)" stroke-width="11"/>
  </svg>
  <div class="brand-name">Brightline Printing</div>

  <h1 class="headline">
    <span class="lead">Your One-Stop</span>
    <span class="main">Creative Print &amp;</span>
    <span class="main">Design Hub</span>
  </h1>

  <section class="service-card card-print">
    <h3>Print Solutions</h3>
    <ul>
      <li>Business Cards</li><li>Flyers</li><li>Brochures</li><li>Postcards</li><li>Invitations</li><li>Labels</li><li>Booklets</li><li>Catalogs</li><li>Notepads &amp; More</li>
    </ul>
  </section>

  <section class="service-card card-large">
    <h3>Large format</h3>
    <ul>
      <li>Banners</li><li>Signs</li><li>Posters</li><li>Decals</li><li>Vehicle Graphics</li><li>Trade Show Displays</li><li>Table Covers</li><li>Canopies</li><li>Blue Prints &amp; More</li>
    </ul>
  </section>

  <section class="service-card card-apparel">
    <h3>Apparel Printing</h3>
    <ul>
      <li>T-shirts</li><li>Hoodies</li><li>Polo Shirts</li><li>Jerseys</li><li>Work Uniforms</li><li>Aprons</li><li>Caps &amp; Hats</li><li>Tote Bags</li><li>Backpacks &amp; More</li>
    </ul>
  </section>

  <section class="service-card card-promo">
    <h3>Promotional Items</h3>
    <ul>
      <li>Awards/Trophies</li><li>Ballons</li><li>Mugs</li><li>Keychains</li><li>Lanyards</li><li>Pens</li><li>Wristbands</li><li>Coasters</li><li>Flags</li><li>Boxes &amp; More</li>
    </ul>
  </section>

  <h2 class="why-title">Why Print with Us?</h2>

  <div class="reason reason-service">
    <h4>Personalized Customer Service</h4>
    <p>Every project is handled with care to align perfectly with your vision and requirement , ensuring satisfaction at every step</p>
  </div>
  <div class="reason reason-shop">
    <h4>One-Stop Shop</h4>
    <p>From initial design to final production , streamline your project with convenience and efficiency</p>
  </div>
  <div class="reason reason-experience">
    <h4>Generations of Experience</h4>
    <p>We bring Wealth of Knowledge and proven practices, ensuring high quality results to every projects</p>
  </div>

  <div class="specialized">
    <h5>Specialized Services</h5>
    <ul>
      <li>Graphic Design</li><li>Direct Mailing</li><li>Laminating</li><li>Binding</li><li>Stress Free Shipping</li>
    </ul>
  </div>

  <div class="trust">
    <span class="claim">A Team you can Trust</span>
    <span class="since">Since 1985!</span>
  </div>

  <svg class="footer-band" width="927" height="150" viewBox="0 0 927 150">
    <defs>
      <linearGradient id="bandFade" x1="0" y1="0" x2="0" y2="1">
        <stop offset="0" stop-color="#0b0b5c" stop-opacity="0"/>
        <stop offset="1" stop-color="#0b0b5c"/>
      </linearGradient>
    </defs>
    <rect x="0" y="0" width="927" height="44" fill="url(#bandFade)"/>
    <rect x="0" y="42" width="927" height="108" fill="var(--navy)"/>
  </svg>

  <div class="footer-text">
    <span class="slogan">Bring Your Brand to Life in Print and Beyond</span>
    <span class="contact">555.014.2277 | art@brightlineprint.com | www.brightlineprint.com</span>
  </div>

</div>
</body>
</html>
```